Single Page Digital Brochure

We are a Sydney based finance company. We lend money to developers. Please see attached example of what we are looking to have produced. We just need a design which can be posted on LINKEDIN

Target Market(s)

Property Developers who are borrowing money

Industry/Entity Type

Finance

Requirements
Must have
• Australian relevant imagery.

TEXT TO INCLUDE:

New Offering from Ferngate Lending
Nice to have
• Design and colour scheme based around our logo (attached)

Please include the same text as the attachment

Please make the design based loosely on the attachment. But do not copy the attachement
Should not have
• Remove Text: 'Settle in under four days'

```html
<!DOCTYPE html>
<html lang="en">
<head>
<meta charset="utf-8">
<title>New Offering from Ferngate Lending</title>
<link rel="stylesheet" href="https://fonts.googleapis.com/css2?family=Raleway:wght@400;600;700&display=swap">
<style>
  :root {
    --ink: #000000;
    --leaf: #9fd57b;
    --leaf-band: #a4d67c;
    --forest: #27452f;
    --mist: #8c8c8c;
    --paper: #ffffff;
    --sky-dark: #36434d;
    --canopy: #2c3a2f;
    --meadow: #34491f;
    --meadow-light: #45602b;
  }
  * { margin: 0; padding: 0; box-sizing: border-box; }
  html, body {
    width: 1200px;
    height: 628px;
    overflow: hidden;
    background: var(--ink);
  }
  .flyer {
    position: relative;
    width: 1200px;
    height: 628px;
    font-family: "Raleway", Arial, sans-serif;
    font-variant-numeric: lining-nums;
    color: var(--paper);
  }
  .brand-panel {
    position: absolute;
    left: 0; top: 0;
    width: 402px;
    height: 580px;
    background: var(--ink);
  }
  .brand {
    position: absolute;
    left: 0; top: 46px;
    width: 418px;
    text-align: center;
  }
  .brand-dot {
    display: block;
    margin: 0 auto 22px;
  }
  .brand-name {
    font-size: 27px;
    font-weight: 400;
    letter-spacing: 1.5px;
    color: var(--mist);
    text-transform: uppercase;
  }
  .headline {
    position: absolute;
    left: 35px;
    top: 260px;
    font-size: 50px;
    font-weight: 700;
    line-height: 54px;
    color: var(--leaf);
    text-transform: uppercase;
    letter-spacing: 0.5px;
  }
  .scene {
    position: absolute;
    left: 402px; top: 0;
    width: 798px;
    height: 580px;
    background: linear-gradient(to bottom,
      var(--sky-dark) 0%,
      var(--canopy) 40%,
      var(--meadow) 72%,
      var(--meadow-light) 100%);
  }
  .deal {
    position: absolute;
    right: 42px;
    top: 46px;
    text-align: right;
  }
  .deal-title {
    font-size: 44px;
    font-weight: 700;
    line-height: 50px;
    color: var(--leaf);
    margin-bottom: 40px;
  }
  .deal-terms {
    list-style: none;
    font-size: 22px;
    font-weight: 600;
    line-height: 26px;
    letter-spacing: 0.2px;
  }
  .deal-terms li { margin-bottom: 26px; }
  .contact-band {
    position: absolute;
    left: 0; top: 580px;
    width: 1200px;
    height: 48px;
    background: var(--leaf-band);
    color: var(--ink);
    font-size: 23px;
    font-weight: 700;
    line-height: 48px;
    text-align: center;
  }
</style>
</head>
<body>
<main class="flyer">
  <div class="scene" role="img" aria-label="Darkened Australian photograph: a large gum tree in a green paddock under a cloudy sky, with a kangaroo leaping across the grass"></div>

  <section class="brand-panel">
    <div class="brand">
      <svg class="brand-dot" width="64" height="64" viewBox="0 0 64 64" aria-hidden="true">
        <circle cx="32" cy="32" r="32" fill="var(--forest)"/>
      </svg>
      <p class="brand-name">Ferngate Lending</p>
    </div>
    <h1 class="headline">New<br>Offering<br>From<br>Ferngate<br>Lending</h1>
  </section>

  <section class="deal">
    <h2 class="deal-title">We did<br>Just Last week</h2>
    <ul class="deal-terms">
      <li>Loan Amount : $ 75,000,00</li>
      <li>Rate : 7.79%</li>
      <li>Term : 12 Months</li>
      <li>LVR : 60%</li>
      <li>Repayment : Capitalized</li>
      <li>Security : 2X Sydney Residential Property</li>
      <li>Purpose : Business Working Capital</li>
    </ul>
  </section>

  <footer class="contact-band">Call Executive today on 02 9000 4187 &nbsp;or&nbsp; hello@ferngatelending.com</footer>
</main>
</body>
</html>
```